Brightford Lingua Partners, LLC

We need a business card that includes information about our business and conveys a reliable business that provides document translation services and interpreters for a variety of corporate and individual clients. We want to come across as professional, reliable, yet approachable. It should include the following on one side:

ESL / ENL Language Classes, Private Lessons, and Online Tutors
PALQE Training and Testing
Translating & Interpreting Services
Contact us about Over-the-Phone Interpreting in over 200 languages
24/7/365
www.brightfordlingua.example

The other side should include (555) 481-3062

Marla Quennick, President
412 Garvin Ave., Ste. 209
Indianapolis, IN 46999
Updates

Please add USA as part of the address. Also, please add mrqquennick@brightfordlinguapartners.example as the e-mail address. Thank you.

Target Market(s)

Business professionals, their families, the international community

Industry/Entity Type

Business

Contact Information for Business Card

24/7/365
www.brightfordlingua.example

(555) 481-3062

Marla Quennick, President
412 Garvin Ave., Ste. 209
Indianapolis, IN 46999
USA

Font styles to use
Sans Serif

Colors

Designer to choose colors to be used in the design.

Requirements
Must have
• See project description
• e-mail address and web address
• Phone number
Nice to have
• a globe
• physical address
Should not have
• Should not have the same color scheme as other agencies in our market in Indiana unless it is blue and black. No purple or yellow.

```html
<!DOCTYPE html>
<html lang="en">
<head>
<meta charset="utf-8">
<title>Brightford Lingua Partners — Business Card</title>
<link rel="stylesheet" href="https://fonts.googleapis.com/css2?family=Crimson+Text:wght@400;600&family=Arimo:wght@400&display=swap">
<style>
  :root {
    --brand-blue: #0b6bb3;
    --brand-black: #111214;
    --card-white: #eeeff2;
    --text-white: #ffffff;
    --text-dark: #15171a;
    --page-bg: #d9dadd;
  }
  * { box-sizing: border-box; margin: 0; padding: 0; }
  html, body { width: 1200px; height: 800px; overflow: hidden; }
  body {
    background: var(--page-bg);
    font-family: "Crimson Text", Georgia, serif;
    position: relative;
  }
  .card {
    position: absolute;
    top: 250px;
    width: 525px;
    height: 300px;
    background: var(--card-white);
    box-shadow: 0 6px 18px rgba(0,0,0,0.18);
    overflow: hidden;
  }
  .card--services { left: 50px; }
  .card--contact { left: 625px; }
  .card__bands { position: absolute; inset: 0; width: 100%; height: 100%; }

  .brand {
    position: absolute;
    display: flex;
    align-items: center;
    gap: 10px;
  }
  .brand__dot {
    width: 42px; height: 42px;
    border-radius: 50%;
    background: var(--brand-blue);
    flex: none;
  }
  .brand__name {
    font-family: "Crimson Text", Georgia, serif;
    font-weight: 400;
    font-size: 19px;
    line-height: 1.05;
    color: var(--text-dark);
  }
  .card--services .brand { left: 150px; top: 34px; }
  .card--contact .brand { left: 200px; top: 222px; }

  .services {
    position: absolute;
    left: 0; right: 0;
    top: 166px;
    text-align: center;
    color: var(--text-white);
  }
  .services__lead { font-size: 13.5px; }
  .services__extras {
    display: flex;
    align-items: center;
    justify-content: center;
    gap: 10px;
    margin: 5px 0 6px;
  }
  .services__rule { width: 80px; height: 2px; background: var(--text-white); }
  .services__small { font-size: 8.5px; line-height: 1.25; }
  .services__contact { font-size: 13.5px; }
  .services__hours { font-size: 12px; margin-top: 1px; }
  .services__web { font-size: 11.5px; letter-spacing: 3px; margin-top: 2px; }

  .person {
    position: absolute;
    left: 0; right: 0;
    top: 14px;
    text-align: center;
    color: var(--text-white);
  }
  .person__name { font-size: 34px; font-weight: 400; line-height: 1.05; }
  .person__title { font-size: 15px; margin-top: 1px; }

  .details {
    position: absolute;
    left: 28px;
    top: 90px;
    width: 290px;
    list-style: none;
    color: var(--text-white);
    font-family: "Arimo", Arial, sans-serif;
    font-size: 10.5px;
    line-height: 1.35;
  }
  .details__item {
    display: flex;
    align-items: flex-start;
    gap: 7px;
    margin-bottom: 4px;
  }
  .details__icon { width: 12px; height: 12px; flex: none; margin-top: 1px; }
</style>
</head>
<body>

<section class="card card--services" aria-label="Services side">
  <svg class="card__bands" viewBox="0 0 525 300" aria-hidden="true">
    <path fill="var(--brand-black)" d="M0,134 H276 Q284,134 287,124 L293,98 H306 L296,150 H0 Z"/>
    <path fill="var(--brand-blue)" d="M0,148 H282 Q290,148 292,138 L299,108 Q302,98 312,98 H525 V300 H0 Z"/>
  </svg>
  <div class="brand">
    <span class="brand__dot"></span>
    <span class="brand__name">Brightford Lingua<br>Partners, LLC</span>
  </div>
  <div class="services">
    <p class="services__lead">ESL / ENL Language Classes, Private Lessons, and Online Tutors</p>
    <div class="services__extras">
      <span class="services__rule"></span>
      <p class="services__small">PALQE Training and Testing<br>Translating &amp; Interpreting Services</p>
      <span class="services__rule"></span>
    </div>
    <p class="services__contact">Contact us about Over the Phone Interpreting in over 200 languages</p>
    <p class="services__hours">24/7/365</p>
    <p class="services__web">www.brightfordlingua.example</p>
  </div>
</section>

<section class="card card--contact" aria-label="Contact side">
  <svg class="card__bands" viewBox="0 0 525 300" aria-hidden="true">
    <path fill="var(--brand-black)" d="M525,122 V140 H350 Q342,140 340,148 L333,190 H318 L326,132 Q328,122 338,122 Z"/>
    <path fill="var(--brand-blue)" d="M0,0 H525 V124 H340 Q332,124 330,134 L324,180 Q322,190 312,190 H0 Z"/>
  </svg>
  <div class="person">
    <h1 class="person__name">Marla Quennick</h1>
    <p class="person__title">President</p>
  </div>
  <ul class="details">
    <li class="details__item">
      <svg class="details__icon" viewBox="0 0 12 16" aria-hidden="true">
        <path fill="var(--text-white)" d="M6,0 C2.7,0 0,2.6 0,5.9 C0,10 6,16 6,16 C6,16 12,10 12,5.9 C12,2.6 9.3,0 6,0 Z M6,8.2 A2.3,2.3 0 1 1 6,3.6 A2.3,2.3 0 1 1 6,8.2 Z"/>
      </svg>
      <p>412 Garvin Ave., Ste. 209<br>Indianapolis, IN 46999<br>USA</p>
    </li>
    <li class="details__item">
      <svg class="details__icon" viewBox="0 0 12 12" aria-hidden="true">
        <path fill="var(--text-white)" d="M2.4,0.3 L4.3,2.6 L3.2,4 Q4.4,6.9 8,8.8 L9.4,7.7 L11.7,9.6 L10.5,11.4 Q9.6,12 8,11.5 Q2,9 0.5,3.6 Q0.1,2 0.8,1.2 Z"/>
      </svg>
      <p>(555) 481-3062</p>
    </li>
    <li class="details__item">
      <svg class="details__icon" viewBox="0 0 12 12" aria-hidden="true">
        <rect x="0.5" y="2" width="11" height="8" rx="1" fill="none" stroke="var(--text-white)" stroke-width="1.2"/>
        <path d="M0.8,2.6 L6,6.6 L11.2,2.6" fill="none" stroke="var(--text-white)" stroke-width="1.2"/>
      </svg>
      <p>mrqquennick@brightfordlinguapartners.example</p>
    </li>
  </ul>
  <div class="brand">
    <span class="brand__dot"></span>
    <span class="brand__name">Brightford Lingua<br>Partners, LLC</span>
  </div>
</section>

</body>
</html>
```